Pale Lantern Double Sided Flyer Design

We need a double sided flyer (1/3 of an A4 which is 99mm x 210mm) developed for our Newcastle(NSW) tour. This flyer will be placed in tourist information centres and hotels. We want it to direct people to our website or be able to make bookings over the phone.

About Us:-
We are a city walking tour company that runs tours day or night. We run both day and night and will incorporate real history / real Pale lantern. Some of the stories will be quite serious i.e.- there are infamous murders from 100 years ago, baffling court cases, even a bit of poetry written by murderers, suicides, love triangles, you name it. We will be telling the historical stories that tourists will not hear from any other tour provider. A bit of darkness, a bit of mystery and a bit of history theme.

We do no go for scares and let the very real stories deliver the entertainment for our guests. Our customers enjoy our tours, but it isn't light fun and frivolity. Our stories are being carefully crafted and are packed with unexpected twists, turns; revelations whilst remaining all 100% true. We deliver deep, rich, engaging stories.

Here are a few samples of quotes from the characters in our stories that may give you an idea of the kind of history we will cover:-

"There were bits of spines, bits of skulls, [and] finger bones spilled out all over the streets - I ended up filling three boxes. Children were playing with them for weeks”

"I had a close shave last night and now I want a close haircut.”

“She's a beautiful child', isn't she? She's the cause of all the trouble.”

“I did it because she would not come home with me.”

"I have killed my wife. I’m glad she’s dead.”

"Stand aside or I'll put a bullet through both of you."

“You villain, I'll teach you to take away my character."

“You’re not dead yet, you bastard!”

Our website, booking form and contact details can be viewed at www.palelantern.com.au

Target Market(s)

Tourists

Industry/Entity Type

Tour

Colors

Designer to choose colors to be used in the design.

Requirements
Must have
• Vertical orientation please.
• Please also include a reference to a discount offer of 25% using the promo code "WICK".
Nice to have
• FRONT FLYER INFORMATION
• - Pale Lantern Logo
• - "I have killed my wife; I'm glad she's dead."
• - Harbourside Hidden Lanes Walk
• - 25% Discount Offer Codeword WICK
• - web address at the base; www.palelantern.com.au
• BACK FLYER INFORMATION
• - "She's a beautiful child', isn't she? She's the cause of all the trouble.
• - Pale Lantern Logo at the base along with the web address www.palelantern.com.au
• - Blurb:- Pale lantern brings back Newcastle's hidden past, the forgotten past, the dark past that may not want to be remembered.
• Real stories from the streets around you. Discover the histories you won't hear anywhere else. The forgotten stories of yesteryear finally get a chance to be told. Through you they get to live again.
Should not have
• GENERAL
• Please do not include the phone number, email address or social media icons. We want to drive online bookings.

```html
<!DOCTYPE html>
<html lang="en">
<head>
<meta charset="utf-8">
<title>Pale Lantern – Double Sided Flyer</title>
<link href="https://fonts.googleapis.com/css2?family=Open+Sans:wght@400;600;700&family=Montserrat:wght@500;600&display=swap" rel="stylesheet">
<style>
  :root {
    --stage: #4b4b4b;
    --paper: #ffffff;
    --ink: #111111;
    --red: #e3262c;
    --red-deep: #b5161b;
    --black: #141414;
    --photo-grey-light: #d6d1cc;
    --photo-grey-dark: #6b655f;
  }
  * { box-sizing: border-box; margin: 0; padding: 0; }
  html, body { width: 1200px; height: 1200px; overflow: hidden; }
  body {
    background: var(--stage);
    font-family: "Open Sans", sans-serif;
    position: relative;
  }
  .flyer {
    position: absolute;
    top: 86px;
    width: 503px;
    height: 1034px;
    overflow: hidden;
    box-shadow: 0 4px 14px rgba(0,0,0,.45);
  }
  .flyer--front { left: 81px; background: var(--paper); }
  .flyer--back {
    left: 628px;
    background: radial-gradient(ellipse at 50% 45%, #ef2c31 0%, var(--red) 45%, var(--red-deep) 100%);
  }
  .abs { position: absolute; }

  /* brand name in place of logo */
  .brand {
    position: absolute;
    left: 0; right: 0;
    display: flex; align-items: center; justify-content: center; gap: 10px;
    font-weight: 600;
    text-transform: uppercase;
    letter-spacing: .5px;
  }
  .brand__dot { width: 14px; height: 14px; border-radius: 50%; }
  .front-brand { top: 96px; font-size: 24px; color: var(--ink); }
  .front-brand .brand__dot { background: var(--ink); }

  .headline {
    position: absolute; left: 0; right: 0; top: 140px;
    text-align: center;
    font-weight: 700;
    font-size: 41px;
    line-height: 56px;
    color: var(--ink);
  }
  .headline em { font-style: normal; color: var(--red); }
  .rule { position: absolute; height: 2px; background: var(--ink); }
  .tour-name {
    position: absolute; left: 0; right: 0; top: 268px;
    text-align: center; font-size: 27px; color: var(--ink);
    letter-spacing: -.2px;
  }
  .front-photo {
    position: absolute; left: 0; top: 320px; width: 503px; height: 640px;
    background: linear-gradient(to bottom, #ffffff 0%, #e6e2de 10%, var(--photo-grey-light) 22%, #a39d97 50%, var(--photo-grey-dark) 100%);
  }
  .offer {
    position: absolute; left: 39px; top: 840px; width: 428px; height: 130px;
    background: var(--black);
    border-radius: 22px 22px 0 0;
    color: #fff; text-align: center;
    font-family: "Montserrat", sans-serif;
  }
  .offer::before {
    content: ""; position: absolute; inset: 6px 6px -10px 6px;
    border: 2px dashed #fff; border-radius: 18px 18px 0 0;
  }
  .offer__title { margin-top: 12px; font-size: 32px; font-weight: 600; letter-spacing: .5px; }
  .offer__code { font-size: 18px; font-weight: 500; margin-top: -2px; letter-spacing: .3px; }

  .waves { position: absolute; left: 0; bottom: 0; width: 503px; height: 140px; }
  .booking {
    position: absolute; left: 0; right: 0;
    text-align: center; color: #fff;
  }
  .booking__label { font-size: 21px; }
  .booking__url {
    display: flex; align-items: center; justify-content: center; gap: 16px;
    font-size: 20px; font-weight: 600; letter-spacing: 2.2px; margin-top: 2px;
  }
  .booking__url::before, .booking__url::after {
    content: ""; width: 66px; height: 2px; background: #fff;
  }
  .front-booking { top: 960px; }
  .back-booking { top: 949px; }

  /* back */
  .photo-circles { position: absolute; left: 0; top: 0; width: 503px; height: 440px; }
  .quote {
    position: absolute; left: 0; right: 0; top: 450px;
    text-align: center; color: #fff; font-weight: 700;
    font-size: 28.5px; line-height: 42px;
  }
  .back-rule { position: absolute; left: 74px; width: 380px; top: 540px; height: 1px; background: rgba(255,255,255,.7); }
  .blurb {
    position: absolute; left: 14px; width: 480px; top: 559px;
    color: #fff; font-size: 18px; line-height: 24.5px; list-style: none;
  }
  .blurb li { position: relative; padding-left: 26px; margin-bottom: 16px; text-align: left; }
  .blurb li p.justified { text-align: justify; text-align-last: left; }
  .blurb .tick { position: absolute; left: 0; top: 5px; width: 18px; height: 14px; }
  .back-brand { top: 867px; font-size: 27px; color: #fff; }
  .back-brand .brand__dot { background: #fff; }
</style>
</head>
<body>

<section class="flyer flyer--front" aria-label="Flyer front">
  <div class="brand front-brand"><span class="brand__dot"></span>Pale Lantern</div>

  <h1 class="headline">I have killed my wife<br>I'm glad <em>she's dead</em></h1>

  <div class="rule" style="left:72px; width:360px; top:259px;"></div>
  <p class="tour-name">Harbourside Hidden Lanes Walk</p>
  <div class="rule" style="left:64px; width:374px; top:316px;"></div>

  <div class="front-photo" role="img" aria-label="Sepia photograph of an old city street with a stone arch bridge and cathedral spire"></div>

  <div class="offer">
    <p class="offer__title">25% Discount Offer</p>
    <p class="offer__code">Codeword WICK</p>
  </div>

  <svg class="waves" viewBox="0 0 503 140" preserveAspectRatio="none" aria-hidden="true">
    <path d="M0,26 C60,0 170,4 251,46 C330,6 450,-4 503,30 L503,140 L0,140 Z" fill="#ffffff"/>
    <path d="M0,42 C60,14 170,18 251,62 C330,20 450,10 503,46 L503,140 L0,140 Z" fill="var(--red)"/>
  </svg>

  <div class="booking front-booking">
    <p class="booking__label">For Booking Please Visit Our Website</p>
    <p class="booking__url">www.palelantern.com.au</p>
  </div>
</section>

<section class="flyer flyer--back" aria-label="Flyer back">
  <svg class="photo-circles" viewBox="0 0 503 440" aria-hidden="false">
    <defs>
      <linearGradient id="skyline" x1="0" y1="0" x2="0" y2="1">
        <stop offset="0" stop-color="#b9d3dc"/>
        <stop offset="0.45" stop-color="#9fb7bd"/>
        <stop offset="0.75" stop-color="#8a7763"/>
        <stop offset="1" stop-color="#5d4e40"/>
      </linearGradient>
      <linearGradient id="riverside" x1="0" y1="0" x2="0" y2="1">
        <stop offset="0" stop-color="#d9b98c"/>
        <stop offset="0.5" stop-color="#7c7c78"/>
        <stop offset="1" stop-color="#4d5a5e"/>
      </linearGradient>
    </defs>
    <circle cx="186" cy="124" r="292" fill="var(--black)"/>
    <circle cx="174" cy="134" r="282" fill="#ffffff"/>
    <circle cx="172" cy="136" r="276" fill="url(#skyline)" role="img" aria-label="Photograph of a Gothic cathedral tower above the city rooftops"/>
    <circle cx="386" cy="326" r="118" fill="var(--black)"/>
    <circle cx="384" cy="326" r="111" fill="#ffffff"/>
    <circle cx="384" cy="326" r="104" fill="url(#riverside)" role="img" aria-label="Photograph of riverside buildings at sunset"/>
  </svg>

  <p class="quote">She's a beautiful child', isn't she?<br>She's the cause of all the trouble.</p>
  <div class="back-rule"></div>

  <ul class="blurb">
    <li>
      <svg class="tick" viewBox="0 0 18 14" aria-hidden="true"><polyline points="2,7 7,12 16,2" fill="none" stroke="#fff" stroke-width="2.6"/></svg>
      <p>Pale lantern brings back Newcastle's hidden past, the forgotten past, the dark past that may not want to be remembered.</p>
    </li>
    <li>
      <svg class="tick" viewBox="0 0 18 14" aria-hidden="true"><polyline points="2,7 7,12 16,2" fill="none" stroke="#fff" stroke-width="2.6"/></svg>
      <p>Real stories from the streets around you. Discover the histories you won't hear anywhere else.</p>
      <p class="justified">The forgotten stories of yesteryear finally get a chance to be told. Through you they get to live again.</p>
    </li>
  </ul>

  <div class="brand back-brand"><span class="brand__dot"></span>Pale Lantern</div>

  <svg class="waves" viewBox="0 0 503 140" preserveAspectRatio="none" aria-hidden="true">
    <path d="M0,38 C60,6 170,8 251,54 C330,10 450,0 503,34 L503,140 L0,140 Z" fill="#ffffff"/>
    <path d="M0,54 C60,22 170,24 251,70 C330,26 450,16 503,50 L503,140 L0,140 Z" fill="var(--black)"/>
  </svg>

  <div class="booking back-booking">
    <p class="booking__label">For Booking Please Visit Our Website</p>
    <p class="booking__url">www.palelantern.com.au</p>
  </div>
</section>

</body>
</html>
```